Economic Order Quantity Brochure and FAQ

I am looking to have a an awesome and creative marketing brochure created that has two pages:

Page # 1 - Markets the program. People must look at this page and must be stunned by how AMAZING the design looks to it. Branded with Birch Toolworks logo, and Pelican logo. Use Birch Toolworks colors for the brochure. Include some of the attached pictures I sent in.

Page # 2 - Frequently asked question page. Branded with Birch Toolworks logo, and Pelican logo. Use Birch Toolworks colors for the brochure.

Target Market(s)

Birch Toolworks Store Owners

Industry/Entity Type

Retail

Font styles to use
Serif

Colors
EB3D1F
EC4F4E
F09395
F8D3D4
FCEDEE

Requirements
Must have
• Eye-Catching, Look Creative and Stand Out!, Must Print on 8.5 x 11" paper, Birch Toolworks Black and Red Colors, Use Birch Toolworks and Pelican Logo, Possibly include some of the pictures I attached

```html
<!DOCTYPE html>
<html lang="en">
<head>
<meta charset="utf-8">
<title>Economic Order Quantity Brochure and FAQ</title>
<link href="https://fonts.googleapis.com/css2?family=Montserrat:wght@600;800;900&family=Open+Sans:wght@400;600;700&display=swap" rel="stylesheet">
<style>
:root{
  --red:#EB3D1F;
  --red-soft:#EC4F4E;
  --pink:#F09395;
  --blush:#F8D3D4;
  --mist:#FCEDEE;
  --ink:#1d1d1f;
  --grey:#5a5a5a;
  --stage:#e6e6e6;
  --white:#ffffff;
  --leaf:#7fb342;
}
*{box-sizing:border-box;margin:0;padding:0}
html,body{width:800px;height:1200px;overflow:hidden}
body{background:var(--stage);font-family:"Open Sans",Arial,sans-serif;color:var(--ink);position:relative}
.spread{position:absolute;top:354px;left:10px;display:flex;gap:20px}
.page{width:380px;height:492px;background:var(--white);position:relative;overflow:hidden;box-shadow:0 2px 6px rgba(0,0,0,.15);display:flex;flex-direction:column}
.masthead{height:44px;display:flex;align-items:center;justify-content:space-between;padding:0 14px;border-bottom:3px solid var(--red)}
.brand{display:flex;align-items:center;gap:5px;font-family:"Montserrat",Arial,sans-serif;font-weight:800;font-size:11px;color:var(--ink)}
.brand-square{width:12px;height:12px;background:var(--red)}
.dept{font-family:"Montserrat",Arial,sans-serif;font-weight:900;font-size:10px;color:var(--red);text-align:right;line-height:1.1}
.hero{background:var(--red);height:138px;display:flex;position:relative}
.hero-text{width:52%;padding:10px 8px 8px 14px;color:var(--white)}
.hero-title{font-family:"Montserrat",Arial,sans-serif;font-weight:900;font-size:14px;line-height:1.05;text-transform:uppercase}
.hero-sub{font-family:"Montserrat",Arial,sans-serif;font-weight:600;font-size:6px;margin-top:4px;letter-spacing:.3px;text-transform:uppercase;color:var(--blush)}
.hero-points{margin-top:8px;list-style:none}
.hero-points li{font-size:5.6px;line-height:1.35;margin-bottom:3px;padding-left:7px;position:relative;font-weight:600}
.hero-points li::before{content:"";position:absolute;left:0;top:2px;width:3px;height:3px;background:var(--white)}
.photo{background:linear-gradient(135deg,#6b4a3a,#a85a3c 45%,#3d6b4a);}
.hero-photo{width:48%;height:100%}
.body{flex:1;display:flex;gap:10px;padding:10px 14px}
.col{flex:1;display:flex;flex-direction:column;gap:6px}
.h3{font-family:"Montserrat",Arial,sans-serif;font-weight:800;font-size:7.5px;color:var(--red);text-transform:uppercase;line-height:1.15}
.p{font-size:5.2px;line-height:1.45;color:var(--grey)}
.panel{background:var(--mist);padding:6px;border-left:2px solid var(--red)}
.results{display:grid;grid-template-columns:1fr 1fr;gap:5px}
.result{display:flex;gap:4px;align-items:flex-start}
.result svg{flex:none}
.result .p{font-size:4.8px}
.quote{background:var(--ink);color:var(--white);padding:6px;font-size:5.2px;line-height:1.45;font-style:italic}
.quote b{display:block;font-style:normal;color:var(--pink);margin-top:2px}
.side-photo{height:58px}
.steps{list-style:none;counter-reset:step;display:flex;flex-direction:column;gap:3px}
.steps li{counter-increment:step;font-size:5px;line-height:1.35;color:var(--grey);padding-left:11px;position:relative}
.steps li::before{content:counter(step);position:absolute;left:0;top:0;width:8px;height:8px;border-radius:50%;background:var(--red);color:var(--white);font-size:5px;font-weight:700;text-align:center;line-height:8px}
.footer{height:38px;background:var(--red);display:flex;align-items:center;justify-content:space-between;padding:0 14px;color:var(--white)}
.call{font-family:"Montserrat",Arial,sans-serif;font-weight:900;font-size:11px;line-height:1}
.call small{display:block;font-size:5.5px;font-weight:600;letter-spacing:.5px}
.web{font-size:6px;font-weight:700}
.partner{display:flex;align-items:center;gap:3px;background:var(--white);padding:3px 5px;font-family:"Montserrat",Arial,sans-serif;font-weight:800;font-size:7px;color:var(--ink)}
.partner-dot{width:7px;height:7px;border-radius:50%;background:var(--leaf)}
.faq-top{display:flex;height:92px}
.faq-heading{width:55%;padding:12px 14px;background:var(--mist)}
.faq-heading .title{font-family:"Montserrat",Arial,sans-serif;font-weight:900;font-size:13px;color:var(--red);line-height:1.05}
.faq-heading .p{margin-top:5px}
.faq-photo{width:45%}
.faq{flex:1;display:grid;grid-template-columns:1fr 1fr;gap:4px 10px;padding:8px 14px;align-content:start}
.qa .q{font-family:"Montserrat",Arial,sans-serif;font-weight:800;font-size:5.6px;color:var(--red);line-height:1.2;margin-bottom:1px}
.qa .p{font-size:4.9px}
</style>
</head>
<body>
<div class="spread">

  <section class="page page-program">
    <header class="masthead">
      <div class="brand"><span class="brand-square"></span>Birch Toolworks</div>
      <div class="dept">STORE SYSTEMS &amp;<br>OPERATIONS</div>
    </header>
    <div class="hero">
      <div class="hero-text">
        <h1 class="hero-title">Economic Order Quantity (EOQ Stick)</h1>
        <p class="hero-sub">Driving optimized stocking levels</p>
        <ul class="hero-points">
          <li>5 minutes per day improves replenishment accuracy</li>
          <li>Cut overstock while keeping key items on the shelf</li>
          <li>Smarter orders that reduce freight and handling costs</li>
        </ul>
      </div>
      <div class="photo hero-photo" role="img" aria-label="Store associate restocking a busy hardware aisle"></div>
    </div>
    <div class="body">
      <div class="col">
        <div class="panel">
          <h3 class="h3">Now available in the Retail Analytics Dashboard</h3>
          <p class="p">Review suggested order quantities for every SKU, compare them with current stock and approve changes in a few clicks from your store dashboard.</p>
        </div>
        <h3 class="h3">Get real results</h3>
        <div class="results">
          <div class="result"><svg width="10" height="10" viewBox="0 0 10 10"><circle cx="5" cy="5" r="5" fill="#EB3D1F"/><path d="M2.7 5.2l1.6 1.5 3-3.3" stroke="#fff" stroke-width="1.1" fill="none"/></svg><p class="p">Lower inventory investment across slow items</p></div>
          <div class="result"><svg width="10" height="10" viewBox="0 0 10 10"><circle cx="5" cy="5" r="5" fill="#EB3D1F"/><path d="M2.7 5.2l1.6 1.5 3-3.3" stroke="#fff" stroke-width="1.1" fill="none"/></svg><p class="p">Higher in-stock rates on top sellers</p></div>
          <div class="result"><svg width="10" height="10" viewBox="0 0 10 10"><circle cx="5" cy="5" r="5" fill="#EB3D1F"/><path d="M2.7 5.2l1.6 1.5 3-3.3" stroke="#fff" stroke-width="1.1" fill="none"/></svg><p class="p">Fewer emergency orders and rush freight</p></div>
          <div class="result"><svg width="10" height="10" viewBox="0 0 10 10"><circle cx="5" cy="5" r="5" fill="#EB3D1F"/><path d="M2.7 5.2l1.6 1.5 3-3.3" stroke="#fff" stroke-width="1.1" fill="none"/></svg><p class="p">Better cash flow for seasonal planning</p></div>
        </div>
        <p class="p">Stores using the program report steadier shelves, cleaner backrooms and more time for customers on the sales floor.</p>
      </div>
      <div class="col">
        <h3 class="h3">What retailers are saying</h3>
        <div class="quote">"Our order sizes finally match how fast items sell. We freed up cash and the shelves look fuller."<b>Store Owner, Midwest</b></div>
        <div class="photo side-photo" role="img" aria-label="Store owner reviewing stock levels on a tablet"></div>
        <h3 class="h3">A 5-step rollout process</h3>
        <ol class="steps">
          <li>Enroll your store through your field consultant</li>
          <li>Review suggested quantities in the dashboard</li>
          <li>Adjust min and max settings where needed</li>
          <li>Approve the updated order parameters</li>
          <li>Track results with weekly reports</li>
        </ol>
      </div>
    </div>
    <footer class="footer">
      <div class="call"><small>CALL US</small>1-800-555-0142</div>
      <div class="web">www.birchtoolworks.com</div>
      <div class="partner"><span class="partner-dot"></span>Pelican</div>
    </footer>
  </section>

  <section class="page page-faq">
    <header class="masthead">
      <div class="brand"><span class="brand-square"></span>Birch Toolworks</div>
      <div class="dept">STORE SYSTEMS &amp;<br>OPERATIONS</div>
    </header>
    <div class="faq-top">
      <div class="faq-heading">
        <h2 class="title">FREQUENTLY ASKED QUESTIONS</h2>
        <p class="p">Answers to the most common questions from store owners about the Economic Order Quantity program.</p>
      </div>
      <div class="photo faq-photo" role="img" aria-label="Hardware store aisle with stocked shelves"></div>
    </div>
    <div class="faq">
      <div class="qa"><p class="q">1. What is Economic Order Quantity?</p><p class="p">A method that sets order sizes to balance carrying costs against ordering costs for each item.</p></div>
      <div class="qa"><p class="q">6. Can I override a suggestion?</p><p class="p">Yes. You always keep final control and can adjust any quantity before approving an order.</p></div>
      <div class="qa"><p class="q">2. How is my EOQ calculated?</p><p class="p">It uses your sales history, cost, pack size and delivery schedule to find the ideal order.</p></div>
      <div class="qa"><p class="q">7. Will this affect promotions?</p><p class="p">Promotional and ad items are handled separately so event stock is not reduced.</p></div>
      <div class="qa"><p class="q">3. Where do I find the data?</p><p class="p">Open the Retail Analytics Dashboard and select the EOQ report under inventory tools.</p></div>
      <div class="qa"><p class="q">8. How often is data refreshed?</p><p class="p">Suggestions update weekly to reflect new sales trends and seasonal changes.</p></div>
      <div class="qa"><p class="q">4. Is there a cost to join?</p><p class="p">No. The program is included for all member stores at no additional fee.</p></div>
      <div class="qa"><p class="q">9. Who supports the program?</p><p class="p">Pelican analysts and your field consultant help with setup and questions.</p></div>
      <div class="qa"><p class="q">5. How long until I see results?</p><p class="p">Most stores notice better in-stock levels within the first two order cycles.</p></div>
      <div class="qa"><p class="q">10. How do I get started?</p><p class="p">Call the support line below or contact your consultant to enroll today.</p></div>
    </div>
    <footer class="footer">
      <div class="call"><small>CALL US</small>1-800-555-0142</div>
      <div class="web">www.birchtoolworks.com</div>
      <div class="partner"><span class="partner-dot"></span>Pelican</div>
    </footer>
  </section>

</div>
</body>
</html>
```